Website design for legal tech start up in Switzerland (B2B)

We are for a legal tech start up in Switzerland called MIVA. We have been running since August 2016. This will be our first live website.

We need a website designed and business card design for our start-up in Switzerland. We also need the Web design to be converted into HTML and CSS files.

Function of website:
• To inform potential customers of our services
• Form a key part of our digital marketing and sales footprint.
• Branding

Please find attached logo.

Reason: Looking for more idea's not necessarily set on blue and grey colours only.

Target Market(s)

B2B tech powered legal services.

Industry/Entity Type

Legal

Contact Information for Business Card

Lean and slick design.

Coding

Coded - Design and coding required

Number of Pages Required

5+ page

Requirements
Must have
• VERY LEAN AND CLEAN DESIGN!
• We have received many great standard designs, but we are looking for something more out-of-the box: You can get inspiration from these designs: http://www.plimbergallery.net/websites/clean/
• Thanks!!
• Easy content management system
• Well structured coding for additional development
• Responsive webpage for all types of devices
• SEO optimized
• Tabs (Home, services, team, careers, blog, contact us)
• Colour scheme complementary to logo
Nice to have
• Look and Design - Approachable, High-tech, Modern
• Easy to add chat bot capability in future
Should not have
• Too busy/ too much clutter
• Not take to long to load

```html
<!DOCTYPE html>
<html lang="en">
<head>
<meta charset="utf-8">
<title>MIVA – Legal Services</title>
<link href="https://fonts.googleapis.com/css2?family=Roboto:ital,wght@0,400;0,500;0,700;1,400&display=swap" rel="stylesheet">
<style>
:root{
  --brand:#2b4a80;
  --brand-deep:#24447c;
  --brand-soft:#4c6b9c;
  --ink:#1f2328;
  --muted:#6b7078;
  --line:#9aa6b8;
  --panel:#f3f4f7;
  --bar:#eeeff2;
  --white:#ffffff;
}
*{box-sizing:border-box;margin:0;padding:0}
html,body{width:1200px;height:2239px;overflow:hidden}
body{font-family:"Roboto",Arial,sans-serif;color:var(--ink);background:var(--white);position:relative}
a{color:inherit;text-decoration:none}

/* hero */
.hero{position:absolute;left:0;top:0;width:1200px;height:543px;overflow:hidden}
.hero-photo{position:absolute;inset:0;background:linear-gradient(100deg,#3a3530 0%,#6d655c 25%,#8a8580 45%,#5e5a58 65%,#2f2c2b 100%)}
.hero-shade{position:absolute;inset:0;background:rgba(20,22,28,.35)}
.topnav{position:absolute;left:0;top:0;width:1200px;height:66px}
.brand{position:absolute;left:55px;top:12px;font-size:38px;font-weight:700;letter-spacing:3px;color:var(--white)}
.menu{position:absolute;left:347px;top:24px;display:flex;gap:32px;font-size:16px;color:var(--white)}
.menu .active{font-weight:700}
.pill{position:absolute;top:16px;height:33px;border-radius:17px;font-size:14px;font-weight:500;display:flex;align-items:center;justify-content:center}
.pill-chat{left:980px;width:53px;border:2px solid var(--white);color:var(--white)}
.pill-eval{left:1039px;width:115px;background:var(--white);color:var(--ink)}
.hero-copy{position:absolute;left:370px;top:230px;width:460px;text-align:center;color:var(--white)}
.hero-copy h1{font-size:19px;font-weight:700;margin-bottom:14px}
.hero-copy p{font-size:11px;line-height:22px;color:#e6e6e6}
.btn-ghost{display:inline-block;border:1.5px solid var(--white);color:var(--white);font-size:12px;font-weight:500;padding:10px 16px;border-radius:3px;margin-top:12px}

/* contact bar */
.contactbar{position:absolute;left:0;top:543px;width:1200px;height:35px;background:var(--bar);border-bottom:1px solid #dcdfe4;font-size:14px;color:var(--muted)}
.contactbar .item{position:absolute;top:9px;display:flex;align-items:center;gap:8px}
.social{position:absolute;top:8px;display:flex;gap:20px;left:1008px}
.social span{width:20px;height:20px;border-radius:3px;display:block}

/* welcome */
.welcome{position:absolute;left:0;top:578px;width:1200px;height:150px;text-align:center}
.welcome .mark{font-size:24px;font-weight:700;letter-spacing:2px;color:var(--ink);margin-top:10px}
.welcome h2{font-size:22px;font-weight:500;margin-top:4px}
.accent{color:var(--brand)}
.dotted{position:absolute;left:52px;width:1096px;border-top:2px dotted var(--line)}
.welcome p{position:absolute;left:52px;top:104px;width:1096px;font-size:13px;line-height:20px}

/* practice areas */
.areas{position:absolute;left:0;top:728px;width:1200px;height:297px;background:var(--panel)}
.tabs{position:absolute;left:295px;top:14px;display:flex;gap:0;font-size:15px;font-weight:500}
.tabs span{padding:13px 18px;border:1px solid transparent}
.tabs .current{border-color:var(--brand);background:var(--white);color:var(--brand);border-radius:2px}
.circles{position:absolute;left:52px;top:93px;width:1096px;display:flex;justify-content:space-between;padding:0 9px}
.circle{width:142px;text-align:center}
.circle .disc{width:140px;height:140px;border-radius:50%;margin:0 auto}
.circle b{display:block;font-size:18px;font-weight:700;margin-top:14px}

/* feature columns */
.features{position:absolute;left:0;top:1025px;width:1200px;height:309px;display:flex}
.feature{width:400px;height:309px;background:var(--brand-soft);color:var(--white);text-align:center;padding:26px 52px 0}
.feature.mid{background:var(--brand-deep)}
.feature h3{font-size:27px;font-weight:500;margin-bottom:22px}
.feature p{font-size:14.5px;line-height:22.5px;height:130px}
.feature .btn-ghost{margin-top:18px;font-size:13px;padding:10px 18px}

/* blog */
.blog{position:absolute;left:0;top:1334px;width:1200px;height:464px}
.section-title{position:absolute;left:0;width:1200px;text-align:center;font-size:22px;font-weight:500}
.cards{position:absolute;left:52px;top:84px;display:flex;gap:28px}
.card{width:254px;height:358px;background:var(--panel)}
.card .pic{height:191px}
.card h4{font-size:18px;font-weight:700;margin:14px 19px 8px}
.card p{font-size:13px;line-height:20px;color:var(--muted);margin:0 19px;height:64px}
.card .meta{margin:14px 19px 0;border-top:1px dotted var(--line);padding-top:10px;display:flex;justify-content:space-between;font-size:11px;color:var(--muted)}

/* testimonials */
.voices{position:absolute;left:0;top:1798px;width:1200px;height:287px;background:var(--panel)}
.quote{position:absolute;top:104px;width:410px;font-size:13px;line-height:20px;color:var(--muted);font-style:italic}
.quote cite{display:block;font-style:normal;color:var(--ink);font-size:13px;font-weight:500;margin-top:8px}
.q-left{left:54px;text-align:right}
.q-right{left:739px}
.avatar{position:absolute;top:105px;width:76px;height:76px;border-radius:50%;background:linear-gradient(160deg,#c9b8a8,#7d6d62)}
.divider{position:absolute;left:600px;top:104px;height:78px;border-left:2px dotted var(--line)}
.skyline{position:absolute;left:0;bottom:0;width:1200px;height:70px}

/* footer */
.footer{position:absolute;left:0;top:2085px;width:1200px;height:154px;background:var(--white)}
.footer-main{position:absolute;left:61px;top:52px;display:flex;align-items:center;gap:27px;font-size:13px;font-weight:500}
.footer-rule{position:absolute;left:52px;top:79px;width:1096px;border-top:1px solid #e1e3e8}
.footer-mark{position:absolute;left:1024px;top:34px;font-size:34px;font-weight:700;letter-spacing:2px;color:var(--ink)}
.footer-links{position:absolute;left:61px;top:95px;display:flex;gap:19px;font-size:11px}
.footer-social{position:absolute;left:566px;top:94px;display:flex;gap:5px}
.footer-social span{width:17px;height:17px;background:var(--brand);border-radius:2px;display:block}
.footer-legal{position:absolute;left:895px;top:95px;display:flex;gap:19px;font-size:11px}
.footer-base{position:absolute;left:0;bottom:0;width:1200px;height:4px;background:var(--brand)}
</style>
</head>
<body>

<header class="hero">
  <div class="hero-photo" role="img" aria-label="Photo of classical stone statues of justice in front of a building facade"></div>
  <div class="hero-shade"></div>
  <nav class="topnav">
    <a class="brand" href="#">MIVA</a>
    <div class="menu">
      <a class="active" href="#">HOME</a><a href="#">SERVICES</a><a href="#">TEAM</a><a href="#">CAREERS</a><a href="#">BLOG</a><a href="#">CONTACT</a>
    </div>
    <a class="pill pill-chat" href="#">Chat</a>
    <a class="pill pill-eval" href="#">Free Evaluation</a>
  </nav>
  <div class="hero-copy">
    <h1>We Provide Legal Help for Felonies</h1>
    <p>At vero eos et accusamus et iusto odio dignissimos ducimus qui blanditiis praesentium voluptatum deleniti atque corrupti quos dolores et quas molestias excepturi sint occaecati cupiditate non provident.</p>
    <a class="btn-ghost" href="#">LEARN MORE</a>
  </div>
</header>

<div class="contactbar">
  <div class="item" style="left:52px">
    <svg width="12" height="12" viewBox="0 0 24 24"><path fill="#8a8f97" d="M6.6 10.8a15 15 0 0 0 6.6 6.6l2.2-2.2c.3-.3.7-.4 1-.2 1.1.4 2.3.6 3.6.6.6 0 1 .4 1 1V20c0 .6-.4 1-1 1A17 17 0 0 1 3 4c0-.6.4-1 1-1h3.5c.6 0 1 .4 1 1 0 1.3.2 2.5.6 3.6.1.3 0 .7-.2 1z"/></svg>
    +41 44 555 01 72
  </div>
  <div class="item" style="left:208px">
    <svg width="13" height="10" viewBox="0 0 26 20"><rect x="1" y="1" width="24" height="18" rx="2" fill="#8a8f97"/><path d="M2 3l11 8 11-8" stroke="#eeeff2" stroke-width="2" fill="none"/></svg>
    hello@mivalegal.ch
  </div>
  <div class="social">
    <span style="background:#3b5a9a"></span>
    <span style="background:#d2533f"></span>
    <span style="background:#3aa1d8;border-radius:50%"></span>
    <svg width="14" height="14" viewBox="0 0 24 24" style="margin-top:3px"><circle cx="10" cy="10" r="6.5" stroke="#8a8f97" stroke-width="2.5" fill="none"/><path d="M15 15l6 6" stroke="#8a8f97" stroke-width="2.5"/></svg>
  </div>
</div>

<section class="welcome">
  <div class="mark">MIVA</div>
  <h2>Welcome! We are <span class="accent">Miva at Law</span></h2>
  <div class="dotted" style="top:82px"></div>
  <p>Sed ut perspiciatis unde omnis iste natus error sit voluptatem accusantium doloremque laudantium, totam rem aperiam, eaque ipsa quae ab illo inventore veritatis et quasi architecto beatae vitae dicta sunt explicabo</p>
</section>

<section class="areas">
  <div class="tabs">
    <span class="current">Criminal Charges</span><span>Estate Planning</span><span>Capital Market</span><span>Personal Injury</span>
  </div>
  <div class="dotted" style="top:75px"></div>
  <div class="circles">
    <div class="circle"><div class="disc" role="img" aria-label="Photo of a gavel and handcuffs" style="background:radial-gradient(circle,#6b5a4c,#221d1a)"></div><b>Criminal Law</b></div>
    <div class="circle"><div class="disc" role="img" aria-label="Photo of hands passing a family icon" style="background:radial-gradient(circle,#d9d2c8,#7b6f65)"></div><b>Family Law</b></div>
    <div class="circle"><div class="disc" role="img" aria-label="Photo of a truck on a road" style="background:linear-gradient(170deg,#b9b3ab,#5d5753)"></div><b>Transport</b></div>
    <div class="circle"><div class="disc" role="img" aria-label="Photo of a businessman in an office" style="background:radial-gradient(circle,#c9ccd2,#4a5260)"></div><b>Employment</b></div>
    <div class="circle"><div class="disc" role="img" aria-label="Photo of a blue water splash" style="background:radial-gradient(circle,#bfe3f5,#1f79b8)"></div><b>Water Rights</b></div>
    <div class="circle"><div class="disc" role="img" aria-label="Photo of an insurance consultation" style="background:radial-gradient(circle,#a7a9ad,#3f4146)"></div><b>Insurance</b></div>
  </div>
</section>

<section class="features">
  <div class="feature">
    <h3>Why Choose Us</h3>
    <p>Sed ut perspiciatis unde omnis iste natus error sit voluptatem accusantium doloremque laudantium, totam rem aperiam, eaque ipsa quae ab illo inventore veritatis et quasi architecto beatae vitae dicta sunt explicabo. Nemo enim ipsam voluptatem quia voluptas.</p>
    <a class="btn-ghost" href="#">LEARN MORE</a>
  </div>
  <div class="feature mid">
    <h3>What You Get</h3>
    <p>At vero eos et accusamus et iusto odio dignissimos ducimus qui blanditiis praesentium voluptatum deleniti atque corrupti quos dolores et quas molestias excepturi sint occaecati cupiditate non provident, similique sunt in culpa qui officia</p>
    <a class="btn-ghost" href="#">LEARN MORE</a>
  </div>
  <div class="feature">
    <h3>Careers at Miva</h3>
    <p>Et harum quidem rerum facilis est et expedita distinctio. Nam libero tempore, cum soluta nobis est eligendi optio cumque nihil impedit quo minus id quod maxime placeat facere possimus, omnis voluptas assumenda est, omnis dolor repellendus temporibus.</p>
    <a class="btn-ghost" href="#">LEARN MORE</a>
  </div>
</section>

<section class="blog">
  <h2 class="section-title" style="top:10px">Latest <span class="accent">Blog &amp; Posts</span></h2>
  <div class="dotted" style="top:51px"></div>
  <div class="cards">
    <article class="card">
      <div class="pic" role="img" aria-label="Photo of a person walking with a backpack" style="background:linear-gradient(120deg,#d9d4cc,#6b4a33)"></div>
      <h4>Standard Post</h4>
      <p>Enim congue blandit. Lorem ipsum dolor sit amet, consectetur adipiscing elit. Quisque...</p>
      <div class="meta"><span>▦ 22 June, 2015</span><span>● 0</span></div>
    </article>
    <article class="card">
      <div class="pic" role="img" aria-label="Photo of a coffee carafe on a table" style="background:linear-gradient(160deg,#e6e4df,#8c8377)"></div>
      <h4>Video Post</h4>
      <p>Ultrices posuere cubilia curae curabitur sit amet tortor ut massa commodo. Vestibulum...</p>
      <div class="meta"><span>▦ 22 June, 2015</span><span>● 0</span></div>
    </article>
    <article class="card">
      <div class="pic" role="img" aria-label="Photo of a cafe table against a brick wall" style="background:linear-gradient(160deg,#8b5a3f,#c9b9a6)"></div>
      <h4>Post with Image</h4>
      <p>Enim congue blandit. Lorem ipsum dolor sit amet, consectetur adipiscing elit. Quisque...</p>
      <div class="meta"><span>▦ 22 June, 2015</span><span>● 0</span></div>
    </article>
    <article class="card">
      <div class="pic" role="img" aria-label="Photo of a leather wallet on a desk" style="background:linear-gradient(160deg,#d8d0c3,#7a5a40)"></div>
      <h4>Image Post</h4>
      <p>Ultrices posuere cubilia curae curabitur sit amet tortor ut massa commodo. Vestibulum...</p>
      <div class="meta"><span>▦ 22 June, 2015</span><span>● 3</span></div>
    </article>
  </div>
</section>

<section class="voices">
  <h2 class="section-title" style="top:18px">What <span class="accent">People Say</span></h2>
  <div class="dotted" style="top:57px"></div>
  <blockquote class="quote q-left">Duis aute irure dolor in reprehenderit in voluptate velit esse cillum dolore eu fugiat nulla pariatur. Excepteur sint occaecat cupidatat non proident, sunt in culpa qui officia deserunt mollit.<cite>Marc Aebi, Operations Manager</cite></blockquote>
  <div class="avatar" role="img" aria-label="Portrait photo of a client" style="left:492px"></div>
  <div class="divider"></div>
  <div class="avatar" role="img" aria-label="Portrait photo of a client" style="left:634px"></div>
  <blockquote class="quote q-right">Provident, similique sunt in culpa qui officia deserunt mollitia animi, id est laborum et dolorum fuga. Et harum quidem rerum facilis est et expedita distinctio. Nam libero tempore, cum soluta nobis.<cite>Nora Keller, Creative Designer</cite></blockquote>
  <div class="skyline" role="img" aria-label="Illustrated city skyline with airport and planes" style="background:linear-gradient(180deg,rgba(43,74,128,0) 0%,rgba(43,74,128,.25) 60%,rgba(43,74,128,.55) 100%)"></div>
</section>

<footer class="footer">
  <div class="footer-main">
    <svg width="13" height="13" viewBox="0 0 24 24"><circle cx="10" cy="10" r="6.5" stroke="#6b7078" stroke-width="2.5" fill="none"/><path d="M15 15l6 6" stroke="#6b7078" stroke-width="2.5"/></svg>
    <a href="#">Help &amp; Contact</a><a href="#">Our Services</a><a href="#">Team</a><a href="#">Careers</a>
  </div>
  <div class="footer-mark">MIVA</div>
  <div class="footer-rule"></div>
  <div class="footer-links"><a href="#">About</a><a href="#">Blog</a><a href="#">Jobs</a><a href="#">Public Policy</a><a href="#">Sitemap</a><a href="#">Chat</a><a href="#">Partners</a></div>
  <div class="footer-social"><span></span><span></span><span></span></div>
  <div class="footer-legal"><span>© 2016–2017</span><a href="#">Privacy</a><a href="#" class="accent">Legal</a><a href="#">Feedback</a></div>
  <div class="footer-base"></div>
</footer>

</body>
</html>
```